Business is called "Pelton Ledger". Accounting and tax services.

I need a flyer for my new business "Pelton Ledger". I am an individual accountant working for himself on the Sunshine Coast in Queensland Australia. I would like to see designs that communicate reliability and trust. I believe my point of difference is that I am always available to my clients and I will cap my number of clients to ensure I can service them properly. Accountants in general seem to have a bad reputation for not responding to clients in a timely fashion, whether by email or phone. This is where I intend to differentiate myself. I have included my business card for ideas on colour and for contact information. I have also included some logo's that should go on the flyer. With the QLA logo, the words "Pelton Ledger is a QLA Business" needs to be written either above, below or to the right hand side (as per the business card).

Target Market(s)

Small business owners and individuals requiring taxation and financials

Industry/Entity Type

Public Accounting

Font styles to use
Serif

Requirements
Must have
• Supplied logo's, accounting style pictures etc
Services: Small Business Taxation
Company & Trust Tax Returns
Rental Property Returns
Capital Gains Tax
Individual Tax Returns
BAS and IAS lodgements
Nice to have
• Needs to convey a sense of being reliable and responds to clients quickly.
Should not have
• My name

```html
<!DOCTYPE html>
<html lang="en">
<head>
<meta charset="utf-8">
<title>Pelton Ledger – Flyer</title>
<link rel="stylesheet" href="https://fonts.googleapis.com/css2?family=Montserrat:wght@300;400;700;800&family=Roboto+Condensed:wght@400&display=swap">
<style>
  :root {
    --ink: #0b0b0b;
    --paper: #e6e3e4;
    --white: #ffffff;
    --text-grey: #3a3a3a;
    --badge-blue: #1d5fa8;
    --badge-gold: #f6d20a;
    --partner-blue: #1ab4e8;
    --photo-light: #e9e2d8;
    --photo-mid: #b9a58c;
    --photo-dark: #5d6f86;
  }
  html, body {
    margin: 0;
    padding: 0;
    overflow: hidden;
    background: var(--paper);
  }
  .flyer {
    position: relative;
    width: 848px;
    height: 1200px;
    overflow: hidden;
    background: var(--paper);
    font-family: "Montserrat", sans-serif;
    color: var(--ink);
  }
  .hero-photo {
    position: absolute;
    left: 0; top: 0;
    width: 848px; height: 537px;
    background: linear-gradient(120deg, var(--photo-light) 0%, #d8cbb9 40%, var(--photo-mid) 70%, var(--photo-dark) 100%);
  }
  .brand-bar {
    position: absolute;
    left: 0; top: 0;
    width: 527px; height: 106px;
  }
  .brand-bar svg { position: absolute; left: 0; top: 0; }
  .brand-mark {
    position: absolute;
    left: 42px; top: 20px;
    width: 62px; height: 62px;
    border: 2px solid var(--white);
    border-radius: 50%;
    box-sizing: border-box;
  }
  .brand-name {
    position: absolute;
    left: 126px; top: 30px;
    margin: 0;
    font-weight: 400;
    font-size: 30px;
    letter-spacing: 6px;
    color: var(--white);
    line-height: 40px;
    white-space: nowrap;
  }
  .location-band {
    position: absolute;
    left: 0; top: 537px;
    width: 848px; height: 132px;
    background: var(--ink);
    color: var(--white);
    text-align: center;
  }
  .location-band h2 {
    margin: 12px 0 0;
    font-weight: 800;
    font-size: 52px;
    line-height: 58px;
    letter-spacing: 0.5px;
  }
  .services {
    position: absolute;
    left: 54px; top: 694px;
    width: 400px;
  }
  .services h3 {
    margin: 0 0 32px 4px;
    font-weight: 800;
    font-size: 31px;
    letter-spacing: 2.5px;
    line-height: 40px;
  }
  .service-list {
    list-style: none;
    margin: 0; padding: 0;
  }
  .service-list li {
    display: flex;
    align-items: center;
    height: 38px;
    font-weight: 300;
    font-size: 21px;
    color: var(--ink);
    white-space: nowrap;
  }
  .service-list li:nth-child(4) { margin-top: 6px; }
  .tick {
    flex: none;
    width: 30px; height: 30px;
    margin-right: 8px;
  }
  .pitch {
    position: absolute;
    left: 481px; top: 684px;
    width: 316px;
    font-weight: 300;
    font-size: 20px;
    line-height: 27.4px;
    color: var(--text-grey);
    text-align: justify;
    hyphens: manual;
  }
  .pitch p { margin: 0 0 27.4px; }
  .accreditation {
    position: absolute;
    left: 58px; top: 1031px;
  }
  .accreditation-badge {
    display: flex;
    width: 164px; height: 72px;
  }
  .accreditation-badge .blue { width: 103px; background: var(--badge-blue); }
  .accreditation-badge .gold { width: 61px; background: var(--badge-gold); }
  .accreditation-caption {
    margin: 4px 0 0;
    font-family: "Roboto Condensed", sans-serif;
    font-size: 15px;
    color: var(--ink);
    white-space: nowrap;
  }
  .partner-badge {
    position: absolute;
    left: 250px; top: 1033px;
    width: 88px; height: 88px;
    border-radius: 50%;
    background: var(--partner-blue);
  }
  .contact-shape { position: absolute; left: 0; top: 0; }
  .contact {
    position: absolute;
    left: 451px; top: 1106px;
    width: 340px;
    color: var(--white);
    text-align: center;
  }
  .contact .phone {
    margin: 0;
    font-weight: 700;
    font-size: 49px;
    line-height: 52px;
    letter-spacing: 0.5px;
  }
  .contact .web {
    margin: 0;
    font-weight: 700;
    font-size: 21px;
    line-height: 24px;
  }
</style>
</head>
<body>
<div class="flyer">
  <div class="hero-photo" role="img" aria-label="Photo of an accountant at a desk working on a laptop and calculator beside a notebook and glasses"></div>

  <header class="brand-bar">
    <svg width="527" height="106" viewBox="0 0 527 106" aria-hidden="true">
      <polygon points="0,0 527,0 486,106 0,106" fill="var(--ink)"/>
    </svg>
    <span class="brand-mark" aria-hidden="true"></span>
    <h1 class="brand-name">PELTON LEDGER</h1>
  </header>

  <section class="location-band">
    <h2>SUNSHINE COAST IN<br>QUEENSLAND AUSTRALIA</h2>
  </section>

  <section class="services">
    <h3>SERVICES</h3>
    <ul class="service-list">
      <li><svg class="tick" viewBox="0 0 30 30" aria-hidden="true"><circle cx="15" cy="15" r="13" fill="none" stroke="var(--ink)" stroke-width="2.4"/><path d="M9 15.5l4 4 8-8.5" fill="none" stroke="var(--ink)" stroke-width="2.6" stroke-linecap="round" stroke-linejoin="round"/></svg>Small Business Taxation</li>
      <li><svg class="tick" viewBox="0 0 30 30" aria-hidden="true"><circle cx="15" cy="15" r="13" fill="none" stroke="var(--ink)" stroke-width="2.4"/><path d="M9 15.5l4 4 8-8.5" fill="none" stroke="var(--ink)" stroke-width="2.6" stroke-linecap="round" stroke-linejoin="round"/></svg>Company &amp; Trust Tax Returns</li>
      <li><svg class="tick" viewBox="0 0 30 30" aria-hidden="true"><circle cx="15" cy="15" r="13" fill="none" stroke="var(--ink)" stroke-width="2.4"/><path d="M9 15.5l4 4 8-8.5" fill="none" stroke="var(--ink)" stroke-width="2.6" stroke-linecap="round" stroke-linejoin="round"/></svg>Rental Property Returns</li>
      <li><svg class="tick" viewBox="0 0 30 30" aria-hidden="true"><circle cx="15" cy="15" r="13" fill="none" stroke="var(--ink)" stroke-width="2.4"/><path d="M9 15.5l4 4 8-8.5" fill="none" stroke="var(--ink)" stroke-width="2.6" stroke-linecap="round" stroke-linejoin="round"/></svg>Capital Gains Tax</li>
      <li><svg class="tick" viewBox="0 0 30 30" aria-hidden="true"><circle cx="15" cy="15" r="13" fill="none" stroke="var(--ink)" stroke-width="2.4"/><path d="M9 15.5l4 4 8-8.5" fill="none" stroke="var(--ink)" stroke-width="2.6" stroke-linecap="round" stroke-linejoin="round"/></svg>Individual Tax Returns</li>
      <li><svg class="tick" viewBox="0 0 30 30" aria-hidden="true"><circle cx="15" cy="15" r="13" fill="none" stroke="var(--ink)" stroke-width="2.4"/><path d="M9 15.5l4 4 8-8.5" fill="none" stroke="var(--ink)" stroke-width="2.6" stroke-linecap="round" stroke-linejoin="round"/></svg>BAS and IAS lodgements</li>
    </ul>
  </section>

  <section class="pitch">
    <p>I believe my point of differ&shy;ence is that I am always avail&shy;able to my clients &amp; I will cap my number of clients to ensure I can service them properly.</p>
    <p>Accountants in general seem to have a bad reputation for not responding to clients in a timely fashion, whether by email or phone.</p>
    <p>This is where I intend to differ&shy;entiate myself.</p>
  </section>

  <div class="accreditation">
    <div class="accreditation-badge" role="img" aria-label="Accreditation badge">
      <span class="blue"></span><span class="gold"></span>
    </div>
    <p class="accreditation-caption">Pelton Ledger is a QLA Business</p>
  </div>

  <div class="partner-badge" role="img" aria-label="Accounting software partner badge"></div>

  <svg class="contact-shape" width="848" height="1200" viewBox="0 0 848 1200" aria-hidden="true">
    <polygon points="407,1105 848,1105 848,1200 0,1200 0,1186 360,1186" fill="var(--ink)"/>
    <polygon points="0,1163 369,1163 361,1178 0,1178" fill="var(--ink)"/>
  </svg>

  <section class="contact">
    <p class="phone">0491 570 156</p>
    <p class="web">www.peltonledger.com.au</p>
  </section>
</div>
</body>
</html>
```